We need a design to be used to promote a Black Friday sale in an optical dispensary. This will be used as an email campaign, point of sale materials including counter cards and window cling.

The email graphic needs to be 4" wide by 6" deep, the counter cards are 9" wide by 6" counter cards and a 16" wide by 20" deep window cling.

The content of the design should include:
1. Offer of 50% Off the price of any BLACK frame with the purchase of prescription lenses all day on Black Friday, November 28.
2. Free lens cleaning solution refills for life

Store Locations:

Meridian Lens Works
18350 Larkspur Pkwy
Rosenberg, TX 77471
281-617-2048
www.larkspurmlw.example

Meridian Lens Works
4817 Cedar Bend Road
Houston TX 77082
(281) 752-3390
www.cedarbendmlw.example

The design should be contemporary and fun, and tie into a "black friday theme" Please incorporate the attached MLW (Meridian Lens Works) logo

```html
<!DOCTYPE html>
<html lang="en">
<head>
<meta charset="utf-8">
<title>Meridian Lens Works – Black Friday</title>
<link rel="stylesheet" href="https://fonts.googleapis.com/css2?family=Open+Sans:wdth,wght@75..100,400..800&family=Oswald:wght@500&family=Smokum&display=swap">
<style>
  :root {
    --ink: #0b0b0b;
    --paper: #ffffff;
    --sale-red: #e8202a;
    --body-text: #111111;
  }
  * { margin: 0; padding: 0; box-sizing: border-box; }
  html, body { width: 825px; height: 1200px; overflow: hidden; background: var(--paper); }
  .flyer {
    position: relative;
    width: 825px;
    height: 1200px;
    overflow: hidden;
    background: var(--paper);
    font-family: "Open Sans", Arial, sans-serif;
    color: var(--body-text);
  }
  .headline-band {
    position: absolute; left: 0; top: 0;
    width: 825px; height: 302px;
    background: var(--ink);
  }
  .brand-mark {
    position: absolute; left: 22px; top: 70px;
    display: flex; align-items: center; gap: 10px;
    font-weight: 700; font-size: 42px; line-height: 1; color: var(--paper);
  }
  .brand-mark .dot {
    width: 24px; height: 24px; border-radius: 50%;
    background: var(--paper);
  }
  .headline { font-weight: 700; line-height: 1; }
  .headline span {
    position: absolute; display: block; white-space: nowrap;
    text-align: center; line-height: 1;
  }
  .headline .keep {
    left: 189px; top: 45px; width: 500px;
    font-size: 90px; font-stretch: 88%; color: var(--paper);
  }
  .headline .and {
    left: 317px; top: 141px; width: 200px;
    font-size: 42px; color: var(--paper);
  }
  .headline .shop {
    left: 160px; top: 183px; width: 500px;
    font-size: 110px; font-stretch: 88%; color: var(--sale-red);
  }
  .event-title {
    position: absolute; left: 0; top: 287px; width: 825px;
    text-align: center; white-space: nowrap;
    font-family: "Oswald", "Arial Narrow", sans-serif;
    font-weight: 500; font-size: 150px; line-height: 1;
    letter-spacing: -3px; color: var(--ink);
    transform: scaleY(1.22); transform-origin: top center;
  }
  .offer {
    position: absolute; left: 0; top: 460px;
    width: 825px; height: 250px;
  }
  .offer-lead {
    font-family: "Open Sans", Arial, sans-serif;
    font-weight: 800; font-size: 30px; fill: var(--ink);
  }
  .offer-figure {
    font-family: "Smokum", Georgia, serif;
    fill: var(--sale-red);
  }
  .terms {
    position: absolute; left: 0; top: 717px; width: 825px;
    text-align: center; white-space: nowrap;
    font-size: 54px; font-stretch: 85%;
    line-height: 68px; color: var(--body-text);
  }
  .terms strong { font-weight: 800; }
  .sale-date {
    position: absolute; left: 0; top: 920px; width: 825px;
    text-align: center; white-space: nowrap;
    font-weight: 700; font-size: 76px; font-stretch: 90%;
    line-height: 1; color: var(--sale-red);
  }
  .perk-band {
    position: absolute; left: 0; top: 1002px; width: 825px; height: 72px;
    background: var(--sale-red); color: var(--paper);
    display: flex; align-items: center; justify-content: center;
    white-space: nowrap;
    font-weight: 700; font-size: 28px; font-stretch: 90%;
  }
  .perk-band .perk-free { font-size: 36px; font-weight: 800; margin-right: 9px; }
  .store-footer {
    position: absolute; left: 0; top: 1074px; width: 825px; height: 126px;
    background: var(--paper);
  }
  .footer-mark {
    position: absolute; left: 50px; top: 42px;
    display: flex; align-items: center; gap: 10px;
    font-weight: 700; font-size: 40px; line-height: 1; color: var(--ink);
  }
  .footer-mark .dot { width: 22px; height: 22px; border-radius: 50%; background: var(--ink); }
  .store-address {
    position: absolute; left: 254px; top: 14px;
    font-style: normal; white-space: nowrap;
    font-size: 23px; line-height: 30px; color: var(--body-text);
  }
  .store-address .store-name { font-weight: 700; font-size: 22px; }
  .store-contact {
    position: absolute; left: 562px; top: 44px;
    white-space: nowrap; color: var(--body-text);
  }
  .store-contact .phone { font-weight: 700; font-size: 29px; line-height: 36px; }
  .store-contact .web { font-size: 17px; line-height: 24px; }
</style>
</head>
<body>
<main class="flyer">
  <header class="headline-band">
    <div class="brand-mark"><span class="dot"></span>MLW</div>
    <h1 class="headline">
      <span class="keep">KEEP CLAM</span>
      <span class="and">AND</span>
      <span class="shop">SHOP ON</span>
    </h1>
  </header>

  <h2 class="event-title">BLACK FRIDAY</h2>

  <svg class="offer" width="825" height="250" viewBox="0 0 825 250">
    <rect x="442" y="160" width="298" height="74" rx="22" fill="#0b0b0b" role="img" aria-label="Black eyeglass frames"/>
    <text class="offer-lead" x="135" y="135" text-anchor="middle" transform="rotate(-90 135 135)" textLength="198" lengthAdjust="spacingAndGlyphs">OFFER OF</text>
    <text class="offer-figure" x="148" y="220" font-size="290" textLength="280" lengthAdjust="spacingAndGlyphs">50%</text>
    <text class="offer-figure" x="479" y="197" font-size="257" textLength="237" lengthAdjust="spacingAndGlyphs">OFF</text>
  </svg>

  <p class="terms">
    the price of any <strong>BLACK</strong> frame with<br>
    the purchase of prescription lenses.<br>
    all day on Black Friday,
  </p>

  <p class="sale-date">NOVEMBER 28.</p>

  <div class="perk-band"><span class="perk-free">FREE</span>lens cleaning solution refills for life</div>

  <footer class="store-footer">
    <div class="footer-mark"><span class="dot"></span>MLW</div>
    <address class="store-address">
      <div class="store-name">MERIDIAN LENS WORKS</div>
      <div>4817 Cedar Bend Road</div>
      <div>Houston TX 77082</div>
    </address>
    <div class="store-contact">
      <div class="phone">(281) 752-3390</div>
      <div class="web">www.cedarbendmlw.example</div>
    </div>
  </footer>
</main>
</body>
</html>
```